Analytics software company needs a business card design

We need a business card design for a global analytics software provider called 'Varnel Software'. Our main focus is developing real estate analysis software. We are open to any color scheme. The final design should be simple, modern, and precise.
Updates

There is one day left in our project and we are still looking forward to receiving additional submissions. We look forward to selecting one of your designs. Thanks.

Industry/Entity Type

Real Estate

```html
<!DOCTYPE html>
<html lang="en">
<head>
<meta charset="utf-8">
<title>Varnel Software — Business Card</title>
<link href="https://fonts.googleapis.com/css2?family=Exo+2:wght@400;500;700;800&display=swap" rel="stylesheet">
<style>
  :root {
    --page-bg: #e9e9eb;
    --card-white: #ffffff;
    --brand-blue: #0f4f8c;
    --brand-blue-deep: #0a3a6b;
    --brand-blue-light: #1d6fb8;
    --ink-dark: #1c2230;
    --on-blue: #ffffff;
  }
  * { box-sizing: border-box; margin: 0; padding: 0; }
  html, body {
    width: 1200px; height: 1054px; overflow: hidden;
    background: var(--page-bg);
    font-family: "Exo 2", sans-serif;
  }
  .canvas { position: relative; width: 1200px; height: 1054px; }
  .card {
    position: absolute; left: 220px; width: 760px; height: 434px;
    background: var(--card-white);
    box-shadow: 0 10px 30px rgba(0,0,0,.18);
    overflow: hidden;
  }
  .card--front { top: 50px; display: flex; align-items: center; justify-content: center; gap: 22px; }
  .card--back { top: 570px; }

  .brand-dot {
    width: 96px; height: 96px; border-radius: 50%;
    background: radial-gradient(circle at 35% 30%, var(--brand-blue-light), var(--brand-blue-deep));
    flex: none;
  }
  .brand-name {
    font-weight: 800; color: var(--brand-blue-deep);
    line-height: .95; font-size: 44px;
  }

  .back-band { position: absolute; inset: 0; }
  .back-brand {
    position: absolute; left: 40px; top: 112px;
    display: flex; align-items: center; gap: 16px;
  }
  .back-brand .brand-dot { width: 84px; height: 84px; }
  .back-brand .brand-name { font-size: 40px; }

  .holder { position: absolute; right: 36px; top: 88px; text-align: right; }
  .holder-name { font-size: 26px; font-weight: 500; color: var(--brand-blue); letter-spacing: 1px; line-height: 1.1; }
  .holder-role { font-size: 17px; font-weight: 500; color: var(--ink-dark); letter-spacing: 1.5px; margin-top: 2px; }

  .address {
    position: absolute; right: 36px; top: 212px; text-align: right;
    color: var(--on-blue); font-size: 17px; line-height: 1.35;
  }

  .contacts {
    position: absolute; left: 30px; top: 292px; list-style: none;
    color: var(--on-blue); font-size: 14px; line-height: 1;
  }
  .contacts li { display: flex; align-items: center; gap: 10px; height: 21px; }
  .contacts svg { width: 13px; height: 13px; flex: none; }
  .contacts .icon-fill { fill: var(--on-blue); }
  .contacts .icon-line { fill: none; stroke: var(--on-blue); stroke-width: 1.4; }
</style>
</head>
<body>
<main class="canvas">

  <section class="card card--front" aria-label="Card front">
    <span class="brand-dot" aria-hidden="true"></span>
    <div class="brand-name">Varnel<br>Software</div>
  </section>

  <section class="card card--back" aria-label="Card back">
    <svg class="back-band" viewBox="0 0 760 434" preserveAspectRatio="none" aria-hidden="true">
      <defs>
        <radialGradient id="bandGlow" cx="0.55" cy="0.55" r="0.7">
          <stop offset="0" stop-color="#1d6fb8"/>
          <stop offset="1" stop-color="#0a3a6b"/>
        </radialGradient>
      </defs>
      <polygon points="0,276 300,276 455,168 760,168 760,408 0,408" fill="url(#bandGlow)"/>
    </svg>

    <div class="back-brand">
      <span class="brand-dot" aria-hidden="true"></span>
      <div class="brand-name">Varnel<br>Software</div>
    </div>

    <div class="holder">
      <div class="holder-name">DANIEL HALE</div>
      <div class="holder-role">GENERAL MANAGER</div>
    </div>

    <div class="address">
      742 Linden Ave<br>
      Tower B, Floor 5
    </div>

    <ul class="contacts">
      <li><svg class="icon-fill" viewBox="0 0 16 16"><path d="M3 1l3 3-2 2c1 2 3 4 5 5l2-2 3 3-2 3C6 14 2 10 1 3z"/></svg>020 481 7735</li>
      <li><svg class="icon-fill" viewBox="0 0 16 16"><path d="M4 0h8v16H4zM5.5 2v10h5V2zM8 13a1 1 0 100 2 1 1 0 000-2z"/></svg>020 481 7735</li>
      <li><svg class="icon-fill" viewBox="0 0 16 16"><path d="M3 1h7l3 3v11H3zM5 7h6v1H5zm0 2h6v1H5zm0 2h6v1H5z"/></svg>020 481 7735</li>
      <li><svg class="icon-fill" viewBox="0 0 16 16"><path d="M1 3h14v10H1zM2 4l6 5 6-5v1L8 10 2 5z"/></svg>hello@varnelsoft.com</li>
      <li><svg class="icon-line" viewBox="0 0 16 16"><circle cx="8" cy="8" r="6.3"/><ellipse cx="8" cy="8" rx="2.6" ry="6.3"/><path d="M1.7 8h12.6"/></svg>www.varnelsoft.com</li>
    </ul>
  </section>

</main>
</body>
</html>
```